■依頼の目的/概要
ハルカゼのlumoraで電子書籍出版をします。

■本の内容
40代女性で話すことや伝えること
自分に自信はないけれど

起業したい、
夢や目標を叶えたい、
という方がターゲットです。

声と潜在意識(心)の力を使う「ひだまりトーン」で
人前で自信をもって伝えられるようになったり
やりたいことがどんどん実現できるようになる方法を
書きました。

声や潜在意識を使ったトレーニング、
実例を用いてお伝えしています。

■デザイン要望
40代女性が好むデザインが希望です。
顔写真も入れていただけたらと思います。
その際、手に持っている音符などは載せないようお願いいたします。

お写真と、電子書籍の文章をお送りいたします。

ご応募、心よりお待ちしております!!!

その他何かご不明な点がございましたら、お気軽にご質問下さい。
よろしくお願いいたします。
タイトルは
響きの名手がひもとく
輝く毎日をつくる心の整え方・磨き方
~ひだまりトーンの秘密~

著者は
ひだまりトーンコンサルタント
さとうれな

どうぞよろしくお願いいたします。
LQS表記では、表紙画像のサイズは 50 MB 未満表紙フ
ァイルの理想的な寸法は 2,560 x 1,600 ピクセルとなっています。

文字が見やすいこと。
女性的な優しいイメージと内容が合うもの、
という視点で選ばせていただきました。

素晴らしい作品ばかりで
選ばせていただくのに時間がかかりました。

短期間にも関わらず
素敵な作品を沢山ご応募いただき
どうもありがとうございました!

心より感謝いたします。

機会がございましたら
またどうぞよろしくお願いいたします。

```html
<!DOCTYPE html>
<html lang="ja">
<head>
<meta charset="utf-8">
<title>輝く毎日をつくる心の整え方・磨き方</title>
<link rel="stylesheet" href="https://fonts.googleapis.com/css2?family=Noto+Sans+JP:wght@500;700;900&display=swap">
<style>
  :root {
    --orange: #ee7d1e;
    --orange-deep: #e06f10;
    --ink: #332c29;
    --brown: #3a2414;
    --yellow: #f8c43c;
    --white: #ffffff;
    --photo-light: #e7e6e4;
    --photo-mid: #b9b6b3;
    --photo-dark: #5a5553;
  }
  html, body { margin: 0; padding: 0; overflow: hidden; }
  body { width: 750px; height: 1200px; background: var(--white); font-family: "Noto Sans JP", sans-serif; }
  .cover { position: relative; width: 750px; height: 1200px; overflow: hidden; background: var(--white); }

  .cover-photo {
    position: absolute; left: 0; top: 0; width: 750px; height: 938px;
    background:
      linear-gradient(100deg, rgba(255,255,255,0.92) 0%, rgba(255,255,255,0.7) 40%, rgba(255,255,255,0) 70%),
      radial-gradient(ellipse at 78% 45%, var(--photo-dark) 0%, var(--photo-mid) 45%, var(--photo-light) 80%);
  }
  .cover-photo::after {
    content: ""; position: absolute; left: 0; right: 0; top: 0; height: 90px;
    background: var(--white);
  }

  .tagline {
    position: absolute; left: 14px; top: 8px; margin: 0; line-height: 1.3;
    font-size: 52px; font-weight: 900; color: var(--orange); letter-spacing: 4px;
  }
  .title { position: absolute; left: 14px; top: 94px; margin: 0; font-weight: 900; color: var(--ink); }
  .title-line { display: block; font-size: 100px; line-height: 1; letter-spacing: 3px; margin-bottom: 14px; }
  .title-line:first-child { font-size: 76px; margin-bottom: 22px; }
  .title-accent { color: var(--orange); }
  .title-small { font-size: 58px; }

  .secret-badge {
    position: absolute; left: 12px; top: 450px; width: 250px; height: 250px; border-radius: 50%;
    background: var(--yellow); display: flex; align-items: center; justify-content: center;
    text-align: center; font-size: 42px; font-weight: 900; color: var(--brown); line-height: 1.3;
  }

  .author-photo {
    position: absolute; left: 288px; top: 728px; width: 190px; height: 190px; border-radius: 50%;
    background: radial-gradient(circle at 50% 40%, #e9d9cf 0%, #c7a28c 60%, #8f6a55 100%);
    border: 6px solid var(--yellow); box-sizing: border-box;
  }
  .author { position: absolute; right: 16px; top: 792px; text-align: right; color: var(--ink); white-space: nowrap; }
  .author-role { display: block; font-size: 26px; font-weight: 700; line-height: 1.2; }
  .author-name { display: block; font-size: 56px; font-weight: 900; letter-spacing: 2px; line-height: 1.2; }

  .bonus-band {
    position: absolute; left: 0; top: 938px; width: 750px; height: 54px;
    background: var(--orange); color: var(--white); white-space: nowrap;
    font-size: 44px; font-weight: 900; letter-spacing: 19px; line-height: 54px; padding-left: 12px; box-sizing: border-box;
  }
  .bonus-list { position: absolute; left: 22px; top: 1004px; margin: 0; padding: 0; list-style: none; color: var(--brown); }
  .bonus-item { font-size: 38px; font-weight: 900; line-height: 50px; height: 50px; margin-bottom: 10px; transform: skewX(-8deg); white-space: nowrap; }
  .bonus-item:nth-child(2) { padding-left: 130px; }
  .bonus-item:nth-child(3) { padding-left: 205px; }
  .bonus-num { font-size: 50px; color: var(--orange-deep); margin-right: 4px; }
</style>
</head>
<body>
<main class="cover">
  <div class="cover-photo" role="img" aria-label="白いブラウスで微笑む女性のポートレート写真"></div>

  <p class="tagline">響きの名手がひもとく</p>
  <h1 class="title">
    <span class="title-line"><span class="title-accent">輝く毎日</span><span class="title-small">をつくる</span></span>
    <span class="title-line">心の整え方・</span>
    <span class="title-line">磨き方</span>
  </h1>

  <div class="secret-badge">ひだまり<br>トーンの<br>秘密</div>

  <div class="author-photo" role="img" aria-label="著者さとうれなの顔写真"></div>
  <div class="author">
    <span class="author-role">ひだまりトーン<br>コンサルタント</span>
    <span class="author-name">さとうれな</span>
  </div>

  <div class="bonus-band">限定３大特典プレゼント</div>
  <ol class="bonus-list">
    <li class="bonus-item"><span class="bonus-num">1.</span>ひだまりトーン診断</li>
    <li class="bonus-item"><span class="bonus-num">2.</span>特別レッスン動画30分</li>
    <li class="bonus-item"><span class="bonus-num">3.</span>アファメーション小冊子</li>
  </ol>
</main>
</body>
</html>
```